Brand new letterhead, business card, email signature etc.

We are a financial company in London, UK. Our website is www.marlowvane.com. We're wanting a complete remodel of the company colours, letter head, business cards, email signatures, etc. Looking to keep the same font for the company name. I have upload a colour palette that we want to work with. We're looking for company letterhead for outgoing letters/ correspondence, letterhead for internal documentation, email signatures, e-letters. etc. Ultimately we will redesign the entire website also. It is important that our clients get a strong, secure, warm, trustworthy, solid feeling and first impression.
Updates

Designs look the same

Target Market(s)

Institutional investors, (ultra) high net worth individuals

Industry/Entity Type

Finance, Invesments banking.

Font styles to use
Other font styles liked:
• Current font is "Champagne & Limousines"

Requirements
Must have
• Must use the colours provided on the PDF uploaded to the portal. The purple = main colour. The red = accent colour.
Nice to have
• Nice to use same font as now for the company name "Quillmoor". Font is "Champagne & Limousines". Nice to have some reference to the old logo flower, but only subtle.
Should not have
• Do not use the colour red from our website. Use the colours provided on the colour palette PDF that I uploaded in the portal.

```html
<!DOCTYPE html>
<html lang="en">
<head>
<meta charset="utf-8">
<title>Quillmoor — Business Card</title>
<link rel="stylesheet" href="https://fonts.googleapis.com/css2?family=Josefin+Sans:wght@300&family=Arimo:ital,wght@0,400;0,700;1,400&display=swap">
<style>
  :root {
    --backdrop: #3a3430;
    --card-white: #f6f6f6;
    --plum: #2b0119;
    --ink: #1a1a1a;
    --accent-red: #d6301f;
    --stamen-red: #c0182c;
    --line-grey: #6a6a6a;
  }
  * { box-sizing: border-box; margin: 0; padding: 0; }
  html, body {
    width: 1200px; height: 716px; overflow: hidden;
    background: var(--backdrop);
  }
  .canvas {
    position: relative; width: 1200px; height: 716px;
    display: flex; align-items: center; justify-content: center; gap: 50px;
  }
  .card {
    position: relative; width: 540px; height: 310px;
    box-shadow: 0 10px 24px rgba(0,0,0,.45);
  }
  .card--front { background: var(--card-white); }
  .card--back { background: var(--plum); }

  .brand {
    position: absolute; left: 30px; top: 30px;
    display: flex; align-items: center; gap: 12px;
  }
  .brand__square {
    width: 40px; height: 40px; border: 1px solid var(--line-grey);
  }
  .brand__name {
    font-family: "Josefin Sans", sans-serif; font-weight: 300;
    font-size: 26px; letter-spacing: 6px; color: #444;
    text-transform: uppercase;
  }

  .contact {
    position: absolute; left: 30px; top: 108px;
    font-family: "Arimo", sans-serif; color: var(--ink);
  }
  .contact__name { font-weight: 700; font-size: 19px; color: #2a0a18; }
  .contact__role { font-style: italic; font-size: 12px; color: var(--accent-red); margin-bottom: 12px; }
  .contact__address { font-size: 12px; line-height: 1.35; margin-bottom: 10px; }
  .contact__list { list-style: none; font-size: 12px; line-height: 1.55; }
  .contact__list li { display: flex; align-items: center; gap: 7px; }
  .contact__list svg { width: 10px; height: 10px; fill: var(--accent-red); }

  .flower-art--front {
    position: absolute; right: 40px; top: 70px; width: 220px; height: 210px;
    border-radius: 50%;
    background: radial-gradient(circle at 55% 50%, #ffffff 0%, #e4e4e4 70%, var(--card-white) 100%);
  }
  .flower-art--back {
    position: absolute; left: 195px; top: 60px; width: 170px; height: 170px;
    border-radius: 50%;
    background: radial-gradient(circle at 55% 50%, #5a2a44 0%, #3e0f29 65%, var(--plum) 100%);
  }
  .back__url {
    position: absolute; left: 0; right: 0; bottom: 38px; text-align: center;
    font-family: "Arimo", sans-serif; font-size: 13px; letter-spacing: 4px;
    color: #ffffff;
  }
</style>
</head>
<body>
<main class="canvas">
  <section class="card card--front">
    <div class="brand">
      <span class="brand__square"></span>
      <span class="brand__name">Quillmoor</span>
    </div>
    <div class="contact">
      <p class="contact__name">Elliot Harrow</p>
      <p class="contact__role">President</p>
      <p class="contact__address">27 Fenwick Lane<br>London EC2V 7QP</p>
      <ul class="contact__list">
        <li><svg viewBox="0 0 10 10"><path d="M2 0h2l1 3-1.5 1a6 6 0 0 0 2.5 2.5L7 5l3 1v2c0 1-1 2-2 2C4 10 0 6 0 2c0-1 1-2 2-2z"/></svg>(020) 7946-0381</li>
        <li><svg viewBox="0 0 10 10"><path d="M0 2h10v6H0z M0 2l5 3.5L10 2" /></svg>name@marlowvane.com</li>
        <li><svg viewBox="0 0 10 10"><circle cx="5" cy="5" r="5"/></svg>www.marlowvane.com</li>
      </ul>
    </div>
    <div class="flower-art--front" role="img" aria-label="Line illustration of an open flower with red-tipped stamens"></div>
  </section>

  <section class="card card--back">
    <div class="flower-art--back" role="img" aria-label="White line illustration of an open flower with red-tipped stamens"></div>
    <p class="back__url">www.marlowvane.com</p>
  </section>
</main>
</body>
</html>
```